Business Card Project

We are a small consulting firm. You can experiment with any design.
Must have:
1) Company name - OLUNDEX International
2) Company slogan - simple solutions for complex problems
3) Name/Title/Phone/Email/WWW/ - use anything you like as an example.

Industry/Entity Type

Business

```html
<!DOCTYPE html>
<html lang="en">
<head>
<meta charset="utf-8">
<title>OLUNDEX International – Business Cards</title>
<link rel="stylesheet" href="https://fonts.googleapis.com/css2?family=Source+Sans+3:wght@300;400;600&display=swap">
<style>
  :root {
    --bg-light: #f4f4f4;
    --bg-dark: #bdbdbd;
    --blue: #0563b0;
    --blue-soft: #2a82c0;
    --ink: #1e1e1e;
    --ink-soft: #3f3f3f;
    --white: #ffffff;
    --text: #4a4a4a;
    --text-strong: #3c3c3c;
    --pale-blue: #dcedf7;
    --pale-grey: #efefef;
    --mark-blue: #1e8fd6;
    --mark-grey: #5e5e5e;
  }
  * { margin: 0; padding: 0; box-sizing: border-box; }
  html, body { width: 1200px; height: 1000px; overflow: hidden; }
  body {
    font-family: "Source Sans 3", sans-serif;
    background: linear-gradient(160deg, var(--bg-light) 0%, #e2e2e2 45%, var(--bg-dark) 100%);
    position: relative;
  }
  .card {
    position: absolute;
    width: 266px;
    height: 466px;
    overflow: hidden;
    box-shadow: 0 0 0 1px rgba(0,0,0,0.08);
  }
  .card--blue  { left: 33px;  top: 268px; background: var(--blue); }
  .card--white { background: var(--white); }
  .card--info-blue { left: 315px; top: 268px; }
  .card--dark  { left: 612px; top: 266px; height: 468px; width: 268px; background: var(--ink); }
  .card--info-grey { left: 901px; top: 268px; }

  .pattern-area {
    position: absolute;
    left: 0; right: 0; top: 138px; bottom: 0;
  }
  .card--blue .pattern-area { background: linear-gradient(180deg, var(--blue) 0%, var(--blue-soft) 60%, var(--blue) 100%); }
  .card--dark .pattern-area { background: linear-gradient(180deg, var(--ink) 0%, var(--ink-soft) 60%, var(--ink) 100%); }
  .card--info-blue .pattern-area { background: linear-gradient(180deg, var(--white) 0%, var(--pale-blue) 70%, var(--white) 100%); }
  .card--info-grey .pattern-area { background: linear-gradient(180deg, var(--white) 0%, var(--pale-grey) 70%, var(--white) 100%); }

  .brand {
    position: absolute;
    left: 22px; top: 64px;
    display: flex; align-items: center; gap: 14px;
  }
  .brand__dot { width: 46px; height: 46px; border-radius: 50%; }
  .brand__name {
    font-weight: 300;
    line-height: 1;
  }
  .brand__name .word { display: block; font-size: 31px; letter-spacing: 1px; }
  .brand__name .sub  { display: block; font-size: 10.5px; letter-spacing: 3.4px; margin-top: 3px; }

  .card--blue .brand__dot, .card--dark .brand__dot { background: var(--white); }
  .card--blue .brand__name, .card--dark .brand__name { color: var(--white); }
  .card--info-blue .brand__dot { background: var(--mark-blue); }
  .card--info-grey .brand__dot { background: var(--mark-grey); }
  .card--white .brand__name { color: var(--mark-grey); }

  .slogan {
    position: absolute;
    left: 28px; top: 115px;
    font-size: 12.5px; color: var(--text);
  }
  .role {
    position: absolute; left: 94px; top: 196px;
    color: var(--text);
  }
  .role__title { font-size: 13.5px; }
  .role__name { font-size: 15.5px; font-weight: 600; color: var(--text-strong); margin-top: 1px; }
  .contact {
    position: absolute; left: 0; right: 0; top: 314px;
    text-align: center; font-size: 13.5px; color: var(--text-strong); line-height: 18px;
  }
  .contact .web { margin-top: 3px; }
</style>
</head>
<body>

  <div class="card card--blue">
    <div class="pattern-area" role="img" aria-label="Large decorative brand pattern in lighter blue tones"></div>
    <div class="brand">
      <span class="brand__dot"></span>
      <span class="brand__name"><span class="word">OLUNDEX</span><span class="sub">INTERNATIONAL</span></span>
    </div>
  </div>

  <div class="card card--white card--info-blue">
    <div class="pattern-area" role="img" aria-label="Faint decorative brand pattern in pale blue and grey"></div>
    <div class="brand">
      <span class="brand__dot"></span>
      <span class="brand__name"><span class="word">OLUNDEX</span><span class="sub">INTERNATIONAL</span></span>
    </div>
    <p class="slogan">Simple solutions for complex problems</p>
    <div class="role">
      <p class="role__title">CEO:</p>
      <p class="role__name">Marco Venti</p>
    </div>
    <div class="contact">
      <p>P:000 0000 0000</p>
      <p>F:000 0000 0000</p>
      <p>E:olundex@consulting.com</p>
      <p class="web">www.olundex.com</p>
    </div>
  </div>

  <div class="card card--dark">
    <div class="pattern-area" role="img" aria-label="Large decorative brand pattern in dark grey tones"></div>
    <div class="brand">
      <span class="brand__dot"></span>
      <span class="brand__name"><span class="word">OLUNDEX</span><span class="sub">INTERNATIONAL</span></span>
    </div>
  </div>

  <div class="card card--white card--info-grey">
    <div class="pattern-area" role="img" aria-label="Faint decorative brand pattern in pale grey"></div>
    <div class="brand">
      <span class="brand__dot"></span>
      <span class="brand__name"><span class="word">OLUNDEX</span><span class="sub">INTERNATIONAL</span></span>
    </div>
    <p class="slogan">Simple solutions for complex problems</p>
    <div class="role">
      <p class="role__title">CEO:</p>
      <p class="role__name">Marco Venti</p>
    </div>
    <div class="contact">
      <p>P:000 0000 0000</p>
      <p>F:000 0000 0000</p>
      <p>E:olundex@consulting.com</p>
      <p class="web">www.olundex.com</p>
    </div>
  </div>

</body>
</html>
```